Need Eye Catching & Visually Stimulating/Out of the Box Web Design REFRESH for an Ecommerce W...

We need a new website design for our company Brindle Table (https://www.brindletable-demo.com/). We DO NOT WANT A BORING STANDARD SITE. This site has to be different, and has to POP!

Logo Files: https://files.example-share.net/folders/k7Qm2RtXw9LpZa4VbN8cYd3Hs6JfUe1Go?view=shared

Website Photos here: https://files.example-share.net/folders/9Tz-WqPl4Rk_bnMaYcVx28sdLhe73oj?view=shared

Websites we like:
https://morvenna.sitecraft-demo.io/
http://crumbvale.com/

We will need the site building Wordpress/Woocommerce and also help with interior pages & installation plug-ins -- see further attachments.

Information about the company:
1. PURPOSE: Why do we exist?
We believe that food is the root source to healthy living.
2. VISION: What future do we want to help create?
A world of healthy and happy people.
3. MISSION: What are we here to do?
Empower every person to utilize food as a means of living a healthy life.

Value Proposition:
Brindle Table develops new food based on the latest science to provide the human body with the proper nutrients for optimal health. Our research based foods target the key health functions that support healthy aging and active lifestyles. Since 2002, we have been innovating and designing our meals to meet the needs for healthy aging to active lifestyles. To help people perform their best, today & in the future.

Objective:
This is a nationwide issue and it's coming to the surface. Food affects people in a number of different ways. Our objective is to create an approachable and sustainable solution that can assist people with a number of ailments. The end result for all of them is feeling a feeling they haven't felt in quite some time. Feeling a refreshed you. Like water for fish, food for humans. Keep it clean and simple so you can focus on enjoying your life.

PHRASES/TAGLINES:
Empowerment Through Food
Real Food, Real Results
Nutrition Made Simple
Not Just Meal Prep, Food Science
A healthier you, delivered to your door
Increase your health and wellness baseline.
Discover the potential of healthier eating
Become the best version of you
It’s incredible what proper nutrition feels like
Taste & feel the difference. Your future self will thank you.
A healthier you is just a meal away
Life Changing results
Overwhelmed with being healthy, stops here.
Designed by doctors, approved by humans
Results Driven Healthy Eating, Delivered to you.
Become the person you deserve to be.
Enjoy the process of becoming a better you

Value Propositions:
We Educate & Empower People Through Food to Live Their Best Life
Sustainable health through proper nutrition… that’s enjoyable too.

Key Statements:
We provide satisfying meals that are nutrient dense & deliver results.
Our meals provide an easy way to enjoy an anti-inflammatory diet that's as satisfying as it is healthy.
Health, fat loss & feeling good through chef-prepared, nutrient-dense, satisfying meals delivered to your door.

PLEASE REVIEW THE ATTACHMENTS.

Industry/Entity Type

See Description & Attachments

Coding

Coded - Design and coding required

Number of Pages Required

5+ page

Font styles to use
Other font styles liked:
• See Description & Attachments

Colors
0094D4
00A9DD
6FCCEA
C7EBF8
E9F6FB
00AB8E
00BBA5
67D7C9
C6EFE9
E9F9F6

Requirements
Must have
Nice to have
Should not have

```html
<!DOCTYPE html>
<html lang="en">
<head>
<meta charset="utf-8">
<title>Brindle Table – Eat Fresh & Healthy</title>
<link href="https://fonts.googleapis.com/css2?family=Josefin+Sans:wght@400;600;700&family=Poppins:ital,wght@0,400;0,500;0,600;1,400&display=swap" rel="stylesheet">
<style>
:root{
  --green-deep:#0c4a3a;
  --green:#00ab8e;
  --green-soft:#67d7c9;
  --green-pale:#e9f9f6;
  --mint:#c6efe9;
  --orange:#f5a623;
  --ink:#1d2a26;
  --muted:#6f7a77;
  --white:#ffffff;
  --line:#dfe9e6;
}
*{box-sizing:border-box;margin:0;padding:0}
html,body{width:1200px;height:4316px;overflow:hidden}
body{font-family:"Poppins",sans-serif;color:var(--ink);background:var(--white);position:relative}
h1,h2,h3,h4,.brand{font-family:"Josefin Sans",sans-serif}

/* nav */
.nav{position:absolute;top:0;left:0;width:1200px;height:90px;display:flex;align-items:center;padding:0 175px;z-index:3}
.brand{display:flex;align-items:center;gap:8px;font-weight:700;font-size:22px;color:var(--green-deep)}
.brand .dot{width:14px;height:14px;border-radius:50%;background:var(--green)}
.menu{display:flex;gap:24px;margin-left:auto;margin-right:40px;font-size:14px;font-weight:500}
.menu a{color:var(--ink);text-decoration:none}
.cart{width:30px;height:30px;border-radius:50%;background:var(--green-pale);display:flex;align-items:center;justify-content:center;margin-right:16px}
.btn{display:inline-flex;align-items:center;justify-content:center;border-radius:20px;font-weight:600;font-size:12px;letter-spacing:.5px;color:var(--white);background:var(--green-deep);text-decoration:none;white-space:nowrap}
.nav .btn{width:126px;height:34px;font-size:13px}

/* hero */
.hero{position:absolute;top:90px;left:0;width:1200px;height:520px;background:radial-gradient(circle at 820px 270px,#eef9f5 0,#fff 420px)}
.hero h1{position:absolute;left:175px;top:140px;font-size:36px;line-height:1.2;color:var(--green-deep);font-weight:700;z-index:2;white-space:nowrap}
.hero p{position:absolute;left:175px;top:240px;width:330px;font-size:12px;line-height:1.6;color:var(--muted);z-index:2}
.hero .btn{position:absolute;left:175px;top:320px;width:130px;height:36px}
.badges{position:absolute;left:175px;top:390px;display:flex;gap:14px}
.badges span{width:40px;height:40px;border-radius:50%;border:2px solid var(--green-soft)}
.hero-photo{position:absolute;left:590px;top:50px;width:480px;height:470px;border-radius:50% 50% 0 0;background:linear-gradient(160deg,#f3f7f6,#dfeee9 60%,#c9e3da)}
.chip{position:absolute;background:var(--white);border-radius:10px;box-shadow:0 6px 20px rgba(12,74,58,.12);font-size:12px;display:flex;align-items:center;gap:8px;padding:8px 12px;z-index:2}
.chip .av{width:28px;height:28px;border-radius:50%;background:var(--mint)}
.stars{color:var(--orange);font-size:10px;letter-spacing:1px}

/* section titles */
.title{position:absolute;left:0;width:1200px;text-align:center;font-size:38px;font-weight:700;color:var(--green-deep);line-height:1.2}

/* category */
.cat-card{position:absolute;top:855px;width:280px;height:345px;background:var(--white);border-radius:14px;box-shadow:0 8px 26px rgba(12,74,58,.1);overflow:hidden}
.cat-card .img{height:240px}
.cat-card .row{display:flex;justify-content:space-between;align-items:center;padding:12px 18px 0}
.cat-card h4{font-size:17px;font-weight:600}
.cat-card small{font-size:10px;color:var(--muted)}
.view{font-size:11px;font-weight:600;color:var(--green-deep)}
.rate{font-size:10px;color:var(--orange)}
.arrow{position:absolute;top:1005px;width:36px;height:36px;border-radius:50%;background:var(--green-pale);display:flex;align-items:center;justify-content:center}

/* meal plans */
.meal h2{position:absolute;left:175px;top:1355px;font-size:38px;line-height:1.25;color:var(--green-deep);font-weight:700;width:420px}
.meal p.lead{position:absolute;left:175px;top:1475px;width:390px;font-size:12px;line-height:1.6;color:var(--muted)}
.step{position:absolute;left:175px;display:flex;gap:16px;align-items:flex-start}
.step .ico{width:46px;height:46px;border-radius:8px;background:var(--green-deep);display:flex;align-items:center;justify-content:center}
.step h4{font-size:16px;font-weight:600;margin-top:2px}
.step p{font-size:11px;color:var(--muted);line-height:1.5;width:150px}
.plate-ring{position:absolute;left:620px;top:1470px;width:430px;height:430px;border-radius:50%;border:2px solid var(--line)}
.plate{position:absolute;left:660px;top:1520px;width:320px;height:320px;border-radius:50%;background:radial-gradient(circle,#f4a37a 0 30%,#c9d98f 45%,#fff 62%,#eef1ef 100%);box-shadow:0 20px 40px rgba(0,0,0,.12)}

/* plans */
.plan{position:absolute;top:2235px;width:275px;height:420px;background:var(--white);border-radius:14px;box-shadow:0 8px 26px rgba(12,74,58,.1);overflow:hidden}
.plan .img{height:215px}
.plan .body{padding:14px 18px}
.price{font-size:18px;font-weight:600;color:var(--green)}
.price small{display:block;font-size:10px;color:var(--muted);font-weight:400}
.plan h4{font-size:15px;margin:8px 0 6px;font-weight:600}
.plan p{font-size:10px;line-height:1.55;color:var(--muted)}
.plan .foot{position:absolute;bottom:16px;left:18px;right:18px;display:flex;justify-content:space-between;align-items:center;font-size:10px;font-weight:600;color:var(--green-deep)}
.plan .btn{width:96px;height:28px;font-size:10px;background:var(--green)}
.plan .btn.alt{background:var(--orange)}

/* testimonials */
.quote-mark{position:absolute;left:175px;top:2830px;width:44px;height:44px;border-radius:50%;background:var(--green-deep);color:var(--white);font-size:30px;font-family:"Josefin Sans",sans-serif;display:flex;align-items:center;justify-content:center;padding-top:12px}
.quote{position:absolute;left:175px;top:2900px;width:400px;font-size:13px;font-style:italic;line-height:1.7;color:var(--muted)}
.quote-name{position:absolute;left:175px;top:3010px;font-size:20px;font-weight:600;color:var(--green-deep);font-family:"Josefin Sans",sans-serif}
.orbit{position:absolute;border-radius:50%;border:2px solid var(--line)}
.person{position:absolute;border-radius:50%}

/* newsletter */
.news{position:absolute;left:175px;top:3370px;width:700px;height:330px;background:var(--green-deep);border-radius:40px 0 0 40px}
.news h2{position:absolute;left:50px;top:100px;font-size:34px;color:var(--white);font-weight:700;letter-spacing:1px}
.news form{position:absolute;left:50px;top:170px;width:440px;height:44px;border:1px solid rgba(255,255,255,.5);border-radius:22px;display:flex;align-items:center;justify-content:space-between;padding:0 4px 0 20px;font-size:12px;color:rgba(255,255,255,.7)}
.news form span.btn{background:var(--white);color:var(--green-deep);width:140px;height:36px}
.news-photo{position:absolute;left:720px;top:3365px;width:340px;height:340px;border-radius:50%;background:radial-gradient(circle at 55% 45%,#a0522d 0,#7fa65a 40%,#e8e2d6 62%,#f4f2ee 100%);border:10px solid var(--white)}

/* footer */
.flinks{position:absolute;left:175px;top:3828px;display:flex;gap:22px;font-size:13px;font-weight:500}
.pays{position:absolute;right:175px;top:3822px;display:flex;gap:22px;font-size:15px;font-weight:700;color:var(--green-deep)}
.fline{position:absolute;left:175px;top:3870px;width:850px;height:1px;background:var(--line)}
.fabout{position:absolute;left:175px;top:3930px;width:260px;font-size:11px;line-height:1.65;color:var(--muted)}
.fbrand{position:absolute;left:480px;top:3990px;width:240px;text-align:center}
.fbrand .brand{justify-content:center;font-size:30px}
.fbrand p{font-size:11px;letter-spacing:3px;font-weight:600;margin-top:10px;color:var(--green-deep)}
.contact{position:absolute;left:830px;top:3935px}
.contact h4{font-size:15px;margin-bottom:16px}
.contact li{list-style:none;display:flex;align-items:center;gap:12px;font-size:11px;color:var(--muted);margin-bottom:16px}
.contact .ic{width:28px;height:28px;border-radius:50%;background:var(--green-deep);display:flex;align-items:center;justify-content:center;flex:none}
.copy{position:absolute;left:0;top:4252px;width:1200px;height:64px;background:var(--green-deep);color:var(--white);font-size:12px;display:flex;align-items:center;justify-content:center}
</style>
</head>
<body>

<header class="nav">
  <div class="brand"><span class="dot"></span>Brindle Table</div>
  <nav class="menu"><a>Home</a><a>About Us</a><a>How It Work</a><a>Shop</a><a>Blog</a><a>Contact</a></nav>
  <span class="cart"><svg width="14" height="14" viewBox="0 0 24 24" fill="none" stroke="#0c4a3a" stroke-width="2"><path d="M3 4h2l2 11h11l2-8H7"/><circle cx="9" cy="20" r="1.5"/><circle cx="17" cy="20" r="1.5"/></svg></span>
  <a class="btn">Sign Up</a>
</header>

<section class="hero">
  <div class="hero-photo" role="img" aria-label="Smiling chef holding a plate of fresh salad"></div>
  <h1>Wake Up Early,<br>Eat Fresh &amp; Healthy</h1>
  <p>Chef-prepared, nutrient-dense meals built on the latest food science and delivered fresh to your door each week, so you can focus on living well.</p>
  <a class="btn">GET STARTED</a>
  <div class="badges"><span></span><span></span><span></span><span></span></div>
  <div class="chip" style="left:900px;top:120px"><span class="av"></span><div><b>Dale Marsh</b><div class="stars">★★★★★</div></div></div>
  <div class="chip" style="left:570px;top:395px;font-weight:500"><svg width="16" height="16" viewBox="0 0 24 24" fill="none" stroke="#00ab8e" stroke-width="2"><path d="M2 7h11v9H2zM13 10h5l3 3v3h-8"/><circle cx="6" cy="18" r="2"/><circle cx="17" cy="18" r="2"/></svg>Fast Delivery</div>
</section>

<h2 class="title" style="top:760px">Brindle Table Category</h2>
<span class="arrow" style="left:110px"><svg width="12" height="12" viewBox="0 0 24 24" fill="none" stroke="#0c4a3a" stroke-width="3"><path d="M15 5l-7 7 7 7"/></svg></span>
<span class="arrow" style="left:1054px"><svg width="12" height="12" viewBox="0 0 24 24" fill="none" stroke="#0c4a3a" stroke-width="3"><path d="M9 5l7 7-7 7"/></svg></span>

<article class="cat-card" style="left:172px">
  <div class="img" role="img" aria-label="Veggie meal prep containers" style="background:linear-gradient(135deg,#2b2b2b,#6b3a5a 50%,#8fb04a)"></div>
  <div class="row"><h4>Veggie</h4><small>dinner</small></div>
  <div class="row"><span class="view">VIEW MENU →</span><span class="rate">★ 4.8</span></div>
</article>
<article class="cat-card" style="left:460px">
  <div class="img" role="img" aria-label="Roasted turkey with sweet potatoes" style="background:linear-gradient(135deg,#c77a3c,#8a4a23 55%,#d9a066)"></div>
  <div class="row"><h4>Turkey</h4><small>dinner</small></div>
  <div class="row"><span class="view">VIEW MENU →</span><span class="rate">★ 4.9</span></div>
</article>
<article class="cat-card" style="left:748px">
  <div class="img" role="img" aria-label="Seafood salmon with greens" style="background:linear-gradient(135deg,#6a7a5a,#e39270 50%,#e7e0d4)"></div>
  <div class="row"><h4>Seafood</h4><small>dinner</small></div>
  <div class="row"><span class="view">VIEW MENU →</span><span class="rate">★ 4.7</span></div>
</article>

<section class="meal">
  <h2>Meal plans made for<br>your lifestyle</h2>
  <p class="lead">Pick a plan that suits your week. Our chefs cook every meal with whole ingredients, balanced portions and flavour you will look forward to, then deliver it chilled and ready.</p>
  <div class="step" style="top:1590px"><span class="ico"><svg width="20" height="20" viewBox="0 0 24 24" fill="none" stroke="#fff" stroke-width="2"><path d="M4 4h16v16H4zM8 9h8M8 13h8M8 17h5"/></svg></span><div><h4>Choose your meals</h4><p>Browse menus of fresh, balanced meals.</p></div></div>
  <div class="step" style="top:1670px"><span class="ico"><svg width="20" height="20" viewBox="0 0 24 24" fill="none" stroke="#fff" stroke-width="2"><path d="M2 7h11v9H2zM13 10h5l3 3v3h-8"/><circle cx="6" cy="18" r="2"/><circle cx="17" cy="18" r="2"/></svg></span><div><h4>We Cook &amp; Deliver</h4><p>Fully cooked meals sent fresh to your door.</p></div></div>
  <div class="step" style="top:1750px"><span class="ico"><svg width="20" height="20" viewBox="0 0 24 24" fill="none" stroke="#fff" stroke-width="2"><path d="M6 3h12v18H6zM6 10h12M9 6v2M9 13v3"/></svg></span><div><h4>Chill &amp; Reheat</h4><p>Refrigerate meals and reheat in 3 minutes.</p></div></div>
  <div class="step" style="top:1830px"><span class="ico"><svg width="20" height="20" viewBox="0 0 24 24" fill="none" stroke="#fff" stroke-width="2"><path d="M5 12l4 4 10-10"/></svg></span><div><h4>Eat &amp; Repeat</h4><p>Enjoy, feel the difference, then repeat.</p></div></div>
  <div class="plate-ring"></div>
  <div class="plate" role="img" aria-label="Grilled salmon with lemon and greens on a white plate"></div>
</section>

<h2 class="title" style="top:2075px">Flexible Plans That<br>Fit Your Life</h2>

<article class="plan" style="left:172px">
  <div class="img" role="img" aria-label="Lean and clean dinner bowls" style="background:linear-gradient(135deg,#d9d2c0,#8fb36a 50%,#e0a96a)"></div>
  <div class="body"><div class="price">$ 29.00 USD<small>per week</small></div><h4>Lean &amp; Clean Dinner</h4><p>Lighter dinners packed with lean protein and fresh vegetables to keep you full and on track.</p></div>
  <div class="foot"><span>10 MEALS</span><span class="btn">CHOOSE PLAN</span></div>
</article>
<article class="plan" style="left:462px">
  <div class="img" role="img" aria-label="Chicken salad with tomatoes and greens" style="background:linear-gradient(135deg,#6e9b3e,#c94a3a 50%,#e7dcc7)"></div>
  <div class="body"><div class="price">$ 29.00 USD<small>per week</small></div><h4>Lean &amp; Clean Dinner</h4><p>Hearty salads and grilled chicken balanced for steady energy through your busiest weeks.</p></div>
  <div class="foot"><span>8 MEALS</span><span class="btn alt">CHOOSE PLAN</span></div>
</article>
<article class="plan" style="left:752px">
  <div class="img" role="img" aria-label="Classic dinner grain bowl" style="background:linear-gradient(135deg,#3a3a3a,#a4733e 45%,#8cb85a)"></div>
  <div class="body"><div class="price">$ 30.00 USD<small>per week</small></div><h4>Classic Dinner</h4><p>Comfort favourites remade with whole ingredients, so every plate is as satisfying as it is healthy.</p></div>
  <div class="foot"><span>6 MEALS</span><span class="btn">CHOOSE PLAN</span></div>
</article>

<h2 class="title" style="top:2740px;font-size:34px">What Others Are Saying</h2>
<div class="quote-mark">“</div>
<p class="quote">"Since switching to these meals I sleep better, feel lighter and finally enjoy eating healthy. Every dish tastes fresh and the weekly delivery makes sticking to my goals easy."</p>
<div class="quote-name">Dale Marsh</div>
<div class="orbit" style="left:680px;top:2850px;width:340px;height:340px"></div>
<div class="orbit" style="left:735px;top:2905px;width:230px;height:230px;background:var(--green-pale);border:none"></div>
<div class="person" role="img" aria-label="Portrait of a smiling customer" style="left:745px;top:2880px;width:210px;height:270px;border-radius:50% 50% 40% 40%;background:linear-gradient(160deg,#d6b89a,#c98f73 60%,#e38d8d)"></div>
<div class="person" role="img" aria-label="Customer avatar" style="left:890px;top:2825px;width:44px;height:44px;background:#c9d6e0"></div>
<div class="person" role="img" aria-label="Customer avatar" style="left:665px;top:2975px;width:40px;height:40px;background:#d8c3b0"></div>
<div class="person" role="img" aria-label="Customer avatar" style="left:985px;top:3065px;width:40px;height:40px;background:#cfd8c8"></div>
<div class="person" role="img" aria-label="Customer avatar" style="left:770px;top:3170px;width:48px;height:48px;background:#d2c0b8"></div>

<section class="news">
  <h2>GET LATEST UPDATES</h2>
  <form><span>Enter Your Email</span><span class="btn">SUBSCRIBE</span></form>
</section>
<div class="news-photo" role="img" aria-label="Grilled steak with asparagus on a plate"></div>

<footer>
  <nav class="flinks"><span>Home</span><span>About Us</span><span>How It Work</span><span>Shop</span><span>Blog</span><span>Contact</span></nav>
  <div class="pays"><span>Vantapay</span><span>Paxwell</span><span>Cirqle Card</span><span>Paxwell</span></div>
  <div class="fline"></div>
  <p class="fabout">Brindle Table creates meals grounded in nutrition science to support healthy ageing and active lifestyles. Every dish is cooked by our chefs with whole ingredients, balanced portions and real flavour, then delivered fresh to your door so eating well becomes the easy part of your day and something you look forward to.</p>
  <div class="fbrand"><div class="brand"><span class="dot"></span>Brindle Table</div><p>EAT BETTER. LIVE BETTER.</p></div>
  <div class="contact">
    <h4>Contact Info</h4>
    <ul>
      <li><span class="ic"><svg width="12" height="12" viewBox="0 0 24 24" fill="none" stroke="#fff" stroke-width="2.5"><path d="M12 22s7-7 7-12a7 7 0 10-14 0c0 5 7 12 7 12z"/><circle cx="12" cy="10" r="2.5"/></svg></span>27 Orchard Lane,<br>Fairmont 00412</li>
      <li><span class="ic"><svg width="12" height="12" viewBox="0 0 24 24" fill="none" stroke="#fff" stroke-width="2.5"><path d="M5 3h4l2 5-3 2a11 11 0 006 6l2-3 5 2v4a2 2 0 01-2 2A17 17 0 013 5a2 2 0 012-2z"/></svg></span>(555) 014-2290</li>
      <li><span class="ic"><svg width="12" height="12" viewBox="0 0 24 24" fill="none" stroke="#fff" stroke-width="2.5"><path d="M3 5h18v14H3zM3 6l9 7 9-7"/></svg></span>hello@brindletable-demo.com</li>
    </ul>
  </div>
  <div class="copy">Copyright © 2022 Brindle Table. All rights reserved.</div>
</footer>

</body>
</html>
```